Anzeigengestaltung für Gas- und Wasserinstallationsunternehmen
Zielgruppe
Gas- und Wasserinstallation, wir bauen, warten und sanieren Bäder und Heizungsanlagen
Wir wollen Leute im Alter 26-45 Jahre ansprechen, mit Berufserfahrung
Aufgabenstellung
Dass wir einen Kundendienstmonteur für Öl- und Gasfeuerung suchen

```html
<!DOCTYPE html>
<html lang="de">
<head>
<meta charset="utf-8">
<title>Stellenanzeige Kundendienstmonteur</title>
<link rel="stylesheet" href="https://fonts.googleapis.com/css2?family=Catamaran:wght@400;600;700&display=swap">
<style>
  :root {
    --page-bg: #c4c4c4;
    --white: #ffffff;
    --photo-dark: #1c0a07;
    --photo-mid: #4a1a0c;
    --fire: #e07a1f;
    --fire-hot: #f6c35a;
    --panel: rgba(8, 28, 18, 0.86);
    --band-green: #17a85a;
    --band-teal: #13998a;
    --band-blue: #1766bb;
  }
  * { margin: 0; padding: 0; box-sizing: border-box; }
  html, body {
    width: 1200px; height: 870px; overflow: hidden;
    background: var(--page-bg);
    font-family: "Catamaran", "Segoe UI", sans-serif;
    color: var(--white);
  }
  .ad {
    position: absolute; left: 30px; top: 28px;
    width: 1138px; height: 808px; overflow: hidden;
    box-shadow: 0 2px 6px rgba(0,0,0,0.35);
    background: var(--photo-dark);
  }
  .hero-photo {
    position: absolute; left: 0; top: 0; width: 1138px; height: 602px;
    background:
      radial-gradient(ellipse 300px 340px at 250px 330px, var(--fire-hot) 0%, var(--fire) 35%, rgba(160,50,15,0.6) 60%, transparent 80%),
      radial-gradient(ellipse 260px 200px at 160px 560px, rgba(240,170,70,0.7), transparent 75%),
      linear-gradient(100deg, var(--photo-mid) 0%, #3a1408 45%, var(--photo-dark) 75%, #5a2a12 100%);
  }
  .headline {
    position: absolute; right: 170px; top: 45px;
    font-size: 52px; font-weight: 700; line-height: 66px; text-align: right;
  }
  .headline span { display: block; }
  .subline {
    position: absolute; right: 75px; top: 174px;
    font-size: 31px; font-weight: 700; line-height: 43px; text-align: right;
  }
  .requirements {
    position: absolute; left: 448px; top: 267px; width: 690px; height: 318px;
    background: var(--panel);
    padding: 16px 20px 0 23px;
  }
  .requirements h2 {
    font-size: 24px; font-weight: 700; line-height: 30px; margin-bottom: 8px;
  }
  .requirements ul { list-style: none; font-size: 17.5px; line-height: 27px; }
  .requirements li { position: relative; padding-left: 18px; }
  .requirements li::before {
    content: ""; position: absolute; left: 2px; top: 11px;
    width: 6px; height: 6px; border-radius: 50%; background: var(--white);
  }
  .requirements li.multiline { line-height: 22px; margin: 3px 0 4px; }
  .requirements li.multiline::before { top: 8px; }
  .contact-band {
    position: absolute; left: 0; top: 602px; width: 1138px; height: 206px;
    background: linear-gradient(90deg, var(--band-green) 0%, var(--band-teal) 50%, var(--band-blue) 100%);
  }
  .brand {
    position: absolute; left: 40px; top: 42px;
    display: flex; align-items: center; gap: 22px;
  }
  .brand-dot { width: 60px; height: 60px; border-radius: 50%; background: var(--white); }
  .brand-name { font-size: 38px; font-weight: 700; letter-spacing: 0.5px; }
  .application {
    position: absolute; left: 563px; top: 21px; width: 560px;
    font-size: 16.5px; line-height: 23px;
  }
  .company {
    position: absolute; left: 42px; top: 114px;
    font-size: 19px; line-height: 26px;
  }
  .company strong { font-weight: 700; }
  .phone, .online {
    position: absolute; top: 141px; font-size: 19px; line-height: 26px;
  }
  .phone { left: 491px; }
  .online { left: 821px; }
</style>
</head>
<body>
  <article class="ad">
    <div class="hero-photo" role="img" aria-label="Foto: Handwerker mit Hammer vor lodernden Flammen auf dunklem Hintergrund"></div>

    <h1 class="headline"><span>Feuer und Flamme</span><span>für Ihren Beruf?</span></h1>
    <p class="subline">Wir auch!<br>Kommen Sie in unser Team.</p>

    <section class="requirements">
      <h2>Wir suchen einen Kundendienstmonteur<br>für Öl- und Gasfeuerung (m/w/d):</h2>
      <ul>
        <li class="multiline">abgeschlossene Ausbildung als Gas-Wasser- oder<br>Anlagenmechaniker/in Sanitär /Heizung</li>
        <li>Berufserfahrung im vorgenannten Ausbildungsfeld</li>
        <li>lösungsorientierte, selbstständige und teamorientierte Arbeitsweise</li>
        <li>Führerschein Klasse B</li>
        <li>aufgeschlossen gegenüber neuen Herausforderungen<br>mit Leidenschaft für den Beruf und dem Service beim Kunden</li>
        <li>Zukunftsorientiertes Denken und Arbeiten</li>
      </ul>
    </section>

    <footer class="contact-band">
      <div class="brand">
        <span class="brand-dot"></span>
        <span class="brand-name">THERMWERK GMBH</span>
      </div>
      <p class="application">Schicken Sie uns Ihre aussagekräftigen Unterlagen (Anschreiben, Lebenslauf mit Lichtbild, Zeugnissen) bitte schriftlich oder kommen Sie nach telefonischer Absprache einfach persönlich vorbei und überzeugen uns. Wir freuen uns auf Sie.</p>
      <address class="company" style="font-style:normal">
        <strong>Thermwerk GmbH</strong><br>
        Gesellschaft für Versorgungsanlagen mbH<br>
        Lindenhofer Str. 12 | 10115 Berlin
      </address>
      <p class="phone">Tel. : +49 (0)30 12 34 - 5600<br>Fax : +49 (0)30 12 34 - 5601</p>
      <p class="online">info@thermwerk-gmbh.de<br>www.thermwerk-gmbh.de</p>
    </footer>
  </article>
</body>
</html>
```